AV GLOSSUM BUSINESS CARD DESIGN PROJECT

We need to utilize our logo that was expertly created on Sketchloom and now need to match this with a business card design.

```html
<!DOCTYPE html>
<html lang="en">
<head>
<meta charset="utf-8">
<title>AV Glossum – Business Card</title>
<link href="https://fonts.googleapis.com/css2?family=Poppins:wght@400;600;700&display=swap" rel="stylesheet">
<style>
  :root {
    --brand-blue: #1057ab;
    --card-dark: #1c1c1c;
    --card-white: #ffffff;
    --text-light: #f2f2f2;
    --stage: #3a3a3a;
  }
  * { margin: 0; padding: 0; box-sizing: border-box; }
  html, body {
    width: 1200px; height: 900px; overflow: hidden;
    background: var(--stage);
    font-family: "Poppins", sans-serif;
  }
  .card {
    position: absolute;
    width: 700px; height: 400px;
    border-radius: 28px;
    overflow: hidden;
    box-shadow: 0 18px 40px rgba(0,0,0,0.45);
  }
  /* Front */
  .card-front {
    left: 110px; top: 40px;
    background: var(--brand-blue);
    display: flex; align-items: center; justify-content: center;
  }
  .brand-name {
    font-weight: 600;
    letter-spacing: 0.12em;
    white-space: nowrap;
  }
  .card-front .brand-name { color: var(--card-white); font-size: 66px; }

  /* Back */
  .card-back {
    left: 390px; top: 460px;
    background: var(--card-dark);
  }
  .emblem-ring {
    position: absolute;
    width: 470px; height: 470px; border-radius: 50%;
    left: 308px; top: -178px;
    background: var(--brand-blue);
  }
  .emblem-disc {
    position: absolute;
    width: 470px; height: 470px; border-radius: 50%;
    left: 320px; top: -182px;
    background: var(--card-white);
  }
  .card-back .brand-name {
    position: absolute;
    left: 390px; width: 270px; top: 150px;
    text-align: center;
    color: var(--brand-blue);
    font-size: 30px;
  }
  .contact-block {
    position: absolute; left: 60px; top: 150px;
    color: var(--text-light);
  }
  .person-name {
    color: var(--brand-blue);
    font-weight: 700; font-size: 26px; line-height: 1.1;
    text-transform: uppercase;
  }
  .person-role { font-size: 17px; margin-bottom: 34px; }
  .address { font-size: 16px; line-height: 1.35; margin-bottom: 26px; }
  .contact-list { list-style: none; font-size: 16px; line-height: 1.6; }
  .contact-list li { display: flex; align-items: center; gap: 10px; }
  .contact-list svg { width: 15px; height: 15px; fill: var(--brand-blue); flex: none; }
</style>
</head>
<body>
  <section class="card card-front" aria-label="Card front">
    <span class="brand-name">AV GLOSSUM</span>
  </section>

  <section class="card card-back" aria-label="Card back">
    <div class="emblem-ring"></div>
    <div class="emblem-disc"></div>
    <span class="brand-name">AV GLOSSUM</span>
    <div class="contact-block">
      <p class="person-name">Darren Kovel</p>
      <p class="person-role">Director</p>
      <p class="address">1048 Riverton, Harbor út<br>12-14. floor 3.</p>
      <ul class="contact-list">
        <li><svg viewBox="0 0 24 24"><path d="M6.6 10.8a15.1 15.1 0 0 0 6.6 6.6l2.2-2.2a1 1 0 0 1 1-.25 11.4 11.4 0 0 0 3.6.57 1 1 0 0 1 1 1V20a1 1 0 0 1-1 1A17 17 0 0 1 3 4a1 1 0 0 1 1-1h3.5a1 1 0 0 1 1 1c0 1.25.2 2.45.57 3.57a1 1 0 0 1-.25 1z"/></svg>+36 30 555 0142</li>
        <li><svg viewBox="0 0 24 24"><path d="M2 5h20v14H2z M2 5l10 8 10-8" stroke="#1c1c1c" stroke-width="1.5"/></svg>info@glossum.hu</li>
        <li><svg viewBox="0 0 24 24"><circle cx="12" cy="12" r="10"/></svg>www.glossum.hu</li>
      </ul>
    </div>
  </section>
</body>
</html>
```